Innovative cookies needs innovative design

We are launching some allergen friendly, vegan and sugar free biscuits, based on hemp, and we need a good label to go with it. More than the label itself is the concept that will then be adapted to all our brand.
If you're up for the challenge, to be part of something significant where to leave your blueprint on, show us what you've got!
Updates

Reason: some good things are coming up, there are some more designers that have saved the project to submit shortly, I would like to see more ideas coming out. So far brightquillworkshop is the one that has more elements we like, followed by elements used by Velto and Brix7waves. Once all designers have submitted we will have a picture big enough to decide who might be our first choice in following up on our re branding. Thanks all for your work.

Target Market(s)

Mums, fitness people, kids, vegan

Industry/Entity Type

Health Product

Font styles to use
Sans Serif
Decorative

Colors
9bcb3c
fbed22
ffc214
f78f20
ec1f27
add136
fbee3f
f04a50
ffcf3e

Requirements
Must have
• Must have a modern, Australian feel, with colours and key bullet points like:
• -100% allergen friendly (gluten, dairy, soy, nuts, eggs, sesame)
• -sugar free
• -school friendly
• -non gmo
• -paleo and vegan friendly
• -Made with organic millet and hemp protein
• Quite bold to understand and to catch attention.
Nice to have
• Some drawings, frames, arrows.
Should not have
• Not be boring.

```html
<!DOCTYPE html>
<html lang="en">
<head>
<meta charset="utf-8">
<title>Healthy Biscuits – Box Label</title>
<link rel="stylesheet" href="https://fonts.googleapis.com/css2?family=Dancing+Script:wght@600&family=Londrina+Outline&family=Pathway+Gothic+One&display=swap">
<style>
  :root {
    --page-bg: #e4e4e8;
    --label-cream: #f8f1c6;
    --label-glow: #fdfcf4;
    --leaf-green: #3f9a2a;
    --blob-green: #2f8a3a;
    --sky-blue: #5bb8dd;
    --berry-red: #ec1f27;
    --sun-yellow: #fbd422;
    --biscuit: #c98d52;
    --biscuit-deep: #a8693a;
    --ink: #222222;
    --white: #ffffff;
  }
  * { box-sizing: border-box; margin: 0; padding: 0; }
  html, body { width: 925px; height: 1200px; overflow: hidden; }
  body { background: var(--page-bg); position: relative; }

  .label {
    position: absolute; left: 20px; top: 358px;
    width: 885px; height: 483px; overflow: hidden;
    background: radial-gradient(ellipse 60% 70% at 50% 42%, var(--label-glow) 0%, var(--label-cream) 80%);
  }
  .label > * { position: absolute; }

  .script { font-family: "Dancing Script", cursive; font-weight: 600; }

  .diet-badge { left: 56px; top: 45px; width: 163px; height: 145px; }
  .diet-badge__wash {
    position: absolute; inset: 0; background: var(--blob-green);
    border-radius: 46% 54% 42% 58% / 52% 40% 60% 48%;
  }
  .diet-badge__text {
    position: absolute; inset: 0; display: flex; align-items: center; justify-content: center;
    text-align: center; color: var(--white); font-size: 28px; line-height: 1.05;
  }

  .biscuit-photo {
    left: 330px; top: 62px; width: 246px; height: 246px; border-radius: 50%;
    background: radial-gradient(circle at 45% 40%, var(--biscuit) 0%, var(--biscuit-deep) 85%);
  }
  .biscuit-frame { left: 314px; top: 46px; width: 278px; height: 278px; }

  .top-sprig { left: 200px; top: 0; width: 150px; height: 22px; background: linear-gradient(90deg, transparent, #f6c0bb, transparent); opacity: .7; }
  .dahlia { left: 720px; top: 86px; width: 165px; height: 216px; border-radius: 50%; background: radial-gradient(circle, #d9ecb8 0%, #b7da8a 70%, transparent 72%); }
  .corner-bloom { left: 2px; top: 379px; width: 90px; height: 100px; border-radius: 50% 50% 40% 60%; background: radial-gradient(circle, #f9cfcb 0%, #f6b0ab 60%, transparent 70%); }
  .corner-leaf { left: 810px; top: 402px; width: 75px; height: 81px; border-radius: 80% 0 80% 0; background: #b9dfc9; }

  .brand-name {
    left: 620px; top: 40px; width: 140px; text-align: center;
    font-size: 36px; line-height: 1; color: var(--ink);
  }

  .claim {
    font-family: "Pathway Gothic One", sans-serif; font-size: 17px;
    letter-spacing: .5px; color: var(--ink); text-transform: uppercase; white-space: nowrap;
  }
  .claim--school { left: 175px; top: 228px; }
  .claim--sugar { left: 63px; top: 351px; }
  .claim--gmo { left: 690px; top: 296px; }

  .product-title {
    left: 208px; top: 312px; width: 455px; text-align: center;
    font-family: "Londrina Outline", sans-serif; font-weight: 400; font-size: 72px; line-height: 1;
    color: var(--berry-red); white-space: nowrap; letter-spacing: 1px;
  }

  .doodles { left: 0; top: 0; width: 885px; height: 483px; }
  .doodle { stroke: var(--ink); stroke-width: 1.4; fill: none; stroke-linecap: round; }

  .ribbon svg { position: absolute; inset: 0; width: 100%; height: 100%; }
  .ribbon__text {
    position: absolute; inset: 0; display: flex; flex-direction: column;
    align-items: center; justify-content: center; color: var(--white);
    line-height: 1; white-space: nowrap;
  }
  .ribbon--allergen { left: 126px; top: 406px; width: 291px; height: 56px; }
  .ribbon--allergen .ribbon__text { font-size: 23px; padding-left: 14px; }
  .ribbon__small { font-family: "Pathway Gothic One", sans-serif; font-weight: 400; font-size: 9px; letter-spacing: .3px; margin-top: 1px; }
  .ribbon--protein { left: 451px; top: 404px; width: 314px; height: 52px; }
  .ribbon--protein .ribbon__text { font-size: 16px; }
</style>
</head>
<body>
  <main class="label">
    <div class="top-sprig" role="img" aria-label="Pink line-drawn leaf sprig"></div>
    <div class="dahlia" role="img" aria-label="Green line-drawn dahlia flower"></div>
    <div class="corner-bloom" role="img" aria-label="Red line-drawn flower bud"></div>
    <div class="corner-leaf" role="img" aria-label="Teal line-drawn leaf"></div>

    <div class="diet-badge">
      <div class="diet-badge__wash" role="img" aria-label="Green watercolour splash with leaf sketches"></div>
      <p class="diet-badge__text script">Paleo and<br>vegan<br>friendly</p>
    </div>

    <div class="biscuit-photo" role="img" aria-label="Photo of golden hemp and millet biscuits"></div>
    <svg class="biscuit-frame" viewBox="0 0 278 278">
      <circle cx="139" cy="139" r="128" fill="none" stroke="var(--sun-yellow)" stroke-width="4"/>
      <circle cx="139" cy="139" r="134" fill="none" stroke="var(--sun-yellow)" stroke-width="2"/>
      <circle cx="142" cy="136" r="122" fill="none" stroke="var(--sun-yellow)" stroke-width="1.5"/>
    </svg>

    <p class="brand-name script">Mira's Pantry</p>

    <p class="claim claim--school">School friendly</p>
    <p class="claim claim--sugar">Sugar free</p>
    <p class="claim claim--gmo">Non GMO</p>

    <svg class="doodles" viewBox="0 0 885 483">
      <path class="doodle" d="M232 254 q-8 6 0 10 q8 4 0 10 q-8 6 2 10"/>
      <path class="doodle" d="M200 350 q8 -10 18 -6 q10 4 4 10 q-6 4 -8 -4 q0 -6 10 -6"/>
      <path class="doodle" d="M160 362 q10 -8 20 -2 m-20 2 l2 -7 m-2 7 l7 1"/>
      <path class="doodle" d="M676 330 q8 -10 14 -2 q6 8 14 -4 q6 -8 14 -8 m0 0 l-6 -2 m6 2 l-3 6"/>
    </svg>

    <h1 class="product-title">Healthy Biscuits</h1>

    <div class="ribbon ribbon--allergen">
      <svg viewBox="0 0 291 56" preserveAspectRatio="none">
        <polygon points="0,8 291,0 287,30 291,52 8,56 30,30" fill="var(--leaf-green)"/>
      </svg>
      <p class="ribbon__text script">100% allergen friendly<span class="ribbon__small">(gluten, dairy, soy, nuts, eggs, sesame)</span></p>
    </div>

    <div class="ribbon ribbon--protein">
      <svg viewBox="0 0 314 52" preserveAspectRatio="none">
        <polygon points="0,0 314,2 294,26 314,50 2,52 20,26" fill="var(--sky-blue)"/>
      </svg>
      <p class="ribbon__text script">Made with organic millet and hemp protein</p>
    </div>
  </main>
</body>
</html>
```